Wedding Invitation : Who helps to design a chic wedding card?

We need a chic invitation design for our wedding invitations.

FRONT

- Name logo : Mirte & Koen
- Wedding date : zaterdag 9 juli 2022
- Quote : forever starts here

BACK

- Wij geven elkaar het ja-woord op zaterdag 9 juli 2022
Translation: We’ll say yes on Saturday 9th of July 2022 in the church of Landskouter
- Timeline with icons:

o JAWOORD (Translation: We say yes)
o 15u00

o RECEPTIE (Translation: Reception)
o 18u30

o DINER (Translation: Dinner)
o 19u30
o Feestzaal Volderhof (Location)

o FEEST (Translation: Dinner)
o 21u30

- Locations:

o Icon of a church:
Landskouter
o Icon of a location:
Feestzaal Volderhof
Kapelmeester Drovenstraat 47B
9820 Merelbeke

- RSVP Gelieve jouw aanwezigheid te bevestigen voor 29 mei 2022
(Translation: Please confirm before 29th of May 2022)

STYLE:

- Rosé gold relief press symbols
- Font style : handwritten or serif name (eg. playfair display)
- Font style: description in a more minimalistic font
- Cards will be in craft or ivory white, text will be in rosé gold relief press or black print

FORMAT
American format (229mm W x 114 mm H)

Target Market(s)

People 25-40 years old

Industry/Entity Type

Wedding / Event

Font styles to use
Serif
Sans Serif
Script

Colors

Designer to choose colors to be used in the design.

Requirements
Must have
• Name logo
Nice to have
• Minimalistic animation / icons
Should not have
• Jungle prints

```html
<!DOCTYPE html>
<html lang="nl">
<head>
<meta charset="utf-8">
<title>Trouwkaart Mirte &amp; Koen</title>
<link href="https://fonts.googleapis.com/css2?family=Parisienne&family=Playfair+Display:wght@400;500;700&display=swap" rel="stylesheet">
<style>
  :root {
    --backdrop: #735546;
    --paper-white: #ffffff;
    --paper-ivory: #eee5da;
    --blush: #f1d4c3;
    --blush-deep: #e9c4ae;
    --sand: #eadccb;
    --rose-gold: #b07a45;
    --ink: #1d1d1d;
    --fold: #f5f000;
  }
  * { box-sizing: border-box; margin: 0; padding: 0; }
  html, body { width: 1200px; height: 1000px; overflow: hidden; }
  body {
    position: relative;
    background: var(--backdrop);
    font-family: "Playfair Display", Georgia, serif;
    color: var(--ink);
  }
  .fold-line {
    position: absolute; left: 390px; top: 359px;
    width: 795px; height: 3px; background: var(--fold);
  }
  .card-inside {
    position: absolute; left: 483px; top: 40px;
    width: 323px; height: 648px; background: var(--paper-white);
  }
  .script {
    font-family: "Parisienne", cursive;
    color: var(--rose-gold);
    font-weight: 400;
  }
  .intro { text-align: center; padding-top: 20px; }
  .intro .script { font-size: 17px; line-height: 1; }
  .date-line {
    font-size: 10.5px; font-weight: 700; letter-spacing: 1px;
    color: var(--rose-gold); margin-top: 4px;
  }
  .timeline { position: absolute; left: 32px; top: 78px; }
  .moment { display: flex; align-items: center; height: 40px; margin-bottom: 16px; }
  .moment:nth-child(4) { margin-top: 4px; }
  .moment svg { width: 38px; height: 38px; flex: none; margin-right: 10px; }
  .moment h3 { font-size: 10.5px; font-weight: 700; line-height: 1.05; }
  .moment p { font-size: 10.5px; line-height: 1.05; }
  .section-title { text-align: center; font-size: 22px; line-height: 1; }
  .locations { position: absolute; left: 0; right: 0; top: 332px; }
  .place { display: flex; align-items: center; padding-left: 34px; margin-top: 10px; }
  .place svg { width: 32px; height: 32px; flex: none; margin-right: 14px; }
  .place strong { font-size: 12px; font-weight: 700; }
  .place p { font-size: 11.5px; line-height: 1.25; }
  .rsvp { position: absolute; left: 32px; right: 32px; top: 477px; }
  .rsvp .section-title { font-size: 26px; letter-spacing: 5px; }
  .rsvp .request { font-size: 11.5px; line-height: 1.35; margin-top: 6px; }
  .name-field { display: flex; align-items: flex-end; margin-top: 8px; }
  .name-field .script { font-size: 18px; line-height: 1; }
  .name-field span.rule { display: block; width: 220px; border-bottom: 1px solid var(--rose-gold); margin-left: 4px; margin-bottom: 3px; }
  .choices { margin-left: 52px; margin-top: 4px; }
  .choice { display: flex; align-items: center; font-size: 10px; height: 22px; }
  .choice i { width: 14px; height: 14px; border: 1px solid var(--rose-gold); margin-right: 8px; }

  .card-front {
    position: absolute; left: 837px; top: 40px;
    width: 323px; height: 648px; background: var(--paper-ivory); overflow: hidden;
  }
  .blush-wash { position: absolute; left: 0; top: 0; width: 323px; height: 400px; }
  .tagline {
    position: absolute; left: 0; right: 0; top: 182px; text-align: center;
    font-size: 20px; transform: rotate(180deg);
  }
  .welcome-frame {
    position: absolute; left: 14px; top: 343px; width: 295px; height: 293px;
    border: 1px solid var(--rose-gold); text-align: center;
  }
  .welcome {
    font-size: 10px; font-weight: 700; letter-spacing: 1.5px; line-height: 1.25;
    color: var(--rose-gold); margin-top: 20px;
  }
  .name-logo {
    font-size: 30px; font-weight: 500; letter-spacing: 2px;
    color: var(--rose-gold); margin-top: 54px;
  }
  .front-date {
    position: absolute; left: 0; right: 0; bottom: 24px;
    font-size: 10.5px; font-weight: 700; letter-spacing: 1.5px; color: var(--rose-gold);
  }
  .front-date::before {
    content: ""; display: block; width: 40px; margin: 0 auto 12px;
    border-top: 1px solid var(--rose-gold);
  }
</style>
</head>
<body>
  <div class="fold-line"></div>

  <section class="card-inside">
    <header class="intro">
      <p class="script">Wij geven elkaar het ja-woord op</p>
      <p class="date-line">ZATERDAG 9 JULI 2022</p>
    </header>

    <ol class="timeline">
      <li class="moment">
        <svg viewBox="0 0 40 40" fill="none" stroke="#1d1d1d" stroke-width="1.6"><circle cx="15" cy="24" r="9"/><circle cx="25" cy="24" r="9"/><path d="M11 12l4-5 4 5z"/></svg>
        <div><h3>JAWOORD</h3><p>15u00</p></div>
      </li>
      <li class="moment">
        <svg viewBox="0 0 40 40" fill="none" stroke="#1d1d1d" stroke-width="1.6"><path d="M8 36V16a12 10 0 0 1 24 0v20"/><path d="M5 36h30"/><path d="M17 12c2-2 4-2 6 0"/></svg>
        <div><h3>RECEPTIE</h3><p>18u30</p></div>
      </li>
      <li class="moment">
        <svg viewBox="0 0 40 40" fill="none" stroke="#1d1d1d" stroke-width="1.6"><circle cx="20" cy="20" r="12"/><circle cx="20" cy="20" r="8"/><path d="M4 8v10M2 8v6a2 2 0 0 0 4 0V8M4 18v16M36 8c-3 3-3 10 0 12v14"/></svg>
        <div><h3>DINER</h3><p>19u30<br>Feestzaal Volderhof</p></div>
      </li>
      <li class="moment">
        <svg viewBox="0 0 40 40" fill="none" stroke="#1d1d1d" stroke-width="1.6"><path d="M9 10h8l-1 12a3 3 0 0 1-6 0zM13 25v10M9 35h8"/><path d="M23 10h8l-1 12a3 3 0 0 1-6 0zM27 25v10M23 35h8"/><path d="M18 4l2 3M22 4l-2 3"/></svg>
        <div><h3>FEEST</h3><p>21u30<br>Feestzaal Volderhof</p></div>
      </li>
    </ol>

    <section class="locations">
      <h2 class="section-title script">Locations</h2>
      <div class="place">
        <svg viewBox="0 0 40 40" fill="none" stroke="#1d1d1d" stroke-width="1.6"><path d="M20 3v6M17 6h6M12 16l8-7 8 7M4 22l8-6h16l8 6M6 22v14h28V22M17 36v-7a3 3 0 0 1 6 0v7M20 19v3"/></svg>
        <strong>Landskouter</strong>
      </div>
      <div class="place">
        <svg viewBox="0 0 40 40" fill="none" stroke="#1d1d1d" stroke-width="1.6"><path d="M20 37s-10-12-10-20a10 10 0 0 1 20 0c0 8-10 20-10 20z"/><circle cx="20" cy="17" r="4"/></svg>
        <p>Feestzaal Volderhof<br>Kapelmeester Drovenstraat 47B<br>9820 Merelbeke</p>
      </div>
    </section>

    <section class="rsvp">
      <h2 class="section-title script">RSVP</h2>
      <p class="request">Gelieve jouw aanwezigheid te bevestigen voor 29 mei 2022</p>
      <div class="name-field"><span class="script">M</span><span class="rule"></span></div>
      <div class="choices">
        <p class="choice"><i></i>accepts with pleasure</p>
        <p class="choice"><i></i>declines with regret</p>
      </div>
    </section>
  </section>

  <section class="card-front">
    <svg class="blush-wash" viewBox="0 0 323 400" role="img" aria-label="Rose-gold glitter rose illustration on a blush watercolour wash">
      <defs>
        <linearGradient id="wash" x1="0" y1="0" x2="0.3" y2="1">
          <stop offset="0" stop-color="#ece0cf"/>
          <stop offset="0.45" stop-color="#f1d4c3"/>
          <stop offset="1" stop-color="#e8c6b2"/>
        </linearGradient>
        <radialGradient id="rosegold" cx="0.35" cy="0.25" r="0.6">
          <stop offset="0" stop-color="#d9b07a" stop-opacity="0.7"/>
          <stop offset="1" stop-color="#d9b07a" stop-opacity="0"/>
        </radialGradient>
      </defs>
      <path d="M0 0h323v290c-40 10-90 30-150 32S60 340 0 360z" fill="url(#wash)"/>
      <path d="M0 0h323v200C250 170 160 90 0 110z" fill="url(#rosegold)"/>
    </svg>
    <p class="tagline script">forever starts here</p>
    <div class="welcome-frame">
      <p class="welcome">WELCOME<br>TO THE WEEDING OF</p>
      <p class="name-logo">MIRTE &amp; KOEN</p>
      <p class="front-date">ZATERDAG 9 JULI 2022</p>
    </div>
  </section>
</body>
</html>
```